Business Cards for IT Consulting Company (Managed Service Provider)

I am looking to have some business cards printed and would like some designs. We are an IT Consulting company based in Vancouver BC. I would like a nice clean and modern look to the cards. I have uploaded all the versions of my logo so parts can be used as needed. Here is a snippit from our website homepage:

Kelbrook Systems Ltd. is an IT Solutions Partner located in Vancouver BC, Canada. We offer IT solutions and support to customers in the greater Vancouver Area. With expertise in Microsoft platforms, as well as Linux and Mac OSX and over 12 years experience in the IT industry, Kelbrook Systems is dedicated to offering our clients top quality service and products. We take pride in the solutions we offer our customers. The greatest compliment a client can give us is to recommend our services.

Kelbrook Systems Ltd. offers a wide range of IT services from onsite service to remote support and managed service solutions. This allows clients to choose the support path that best suits their company’s needs. Supporting many different sized companies from small to enterprise level over the past 12 years Kelbrook Systems has the experience and expertise needed to ensure things run smoothly. Allowing our clients to focus on doing business.

Revolutionizing the way IT services are delivered.

Kelbrook Systems is dedicated to providing our clients with IT solutions that work and grow with them for years to come. This philosophy helps save money in the long run instead of replacing equipment constantly. Far too often IT solutions are not well thought out and while possibly solving the problem at hand, require replacement due to growth or quality within a very short time frame. Kelbrook Systems takes pride in providing solutions that will last and be able to accommodate growth without the need for replacement.

Industry/Entity Type

Information Technology

Contact Information for Business Card

Kelbrook Systems Ltd.
(Employee Name)
Eml: (Employees Email Address)
Web: kelbrook.me
Ph: 604-555-0142

Font styles to use
Serif
Sans Serif

Requirements
Must have
• The Company logo and company colors.
Nice to have
• - Our tag line: "Revolutionizing IT Services" or "Revolutionizing the way IT services are delivered."
• - Also I really like the idea of nature and technology together blending which is sort of where my logo came from so integrating that somehow onto the business cards would be great.

```html
<!DOCTYPE html>
<html lang="en">
<head>
<meta charset="utf-8">
<title>Kelbrook Systems – Business Card</title>
<link rel="stylesheet" href="https://fonts.googleapis.com/css2?family=Montserrat:wght@600&family=Open+Sans:wght@400;600&display=swap">
<style>
  :root {
    --sky: #03a3e8;
    --navy: #145e87;
    --steel: #3d7bbf;
    --mist: #9fc0d2;
    --white: #ffffff;
    --crop: #333333;
  }
  * { margin: 0; padding: 0; box-sizing: border-box; }
  html, body { width: 1200px; height: 1200px; overflow: hidden; background: var(--white); }
  .canvas { position: relative; width: 1200px; height: 1200px; font-family: "Open Sans", sans-serif; }
  .crop-mark { position: absolute; width: 26px; height: 24px; border-color: var(--crop); border-style: solid; border-width: 0; }
  .crop-mark--left { left: 202px; top: 84px; border-top-width: 1px; border-left-width: 1px; }
  .crop-mark--right { left: 972px; top: 84px; border-top-width: 1px; border-right-width: 1px; }

  .brand { position: absolute; left: 0; width: 1200px; top: 282px; display: flex; justify-content: center; align-items: center; gap: 18px; }
  .brand__mark { width: 40px; height: 40px; border: 4px solid var(--sky); }
  .brand__name { font-size: 46px; font-weight: 600; color: var(--sky); letter-spacing: 0.5px; }

  .tagline { position: absolute; left: 202px; top: 512px; width: 796px; height: 58px; background: var(--sky); color: var(--white); font-size: 29px; display: flex; align-items: center; justify-content: center; }

  .band { position: absolute; left: 202px; width: 796px; }
  .band--top { top: 629px; height: 112px; background: linear-gradient(90deg, var(--navy), var(--steel)); }
  .band--bottom { top: 1082px; height: 32px; background: linear-gradient(90deg, var(--steel), var(--mist) 50%, var(--navy)); }

  .person { position: absolute; left: 0; width: 1200px; top: 818px; text-align: center; color: var(--sky); }
  .person__name { display: inline-block; font-family: "Montserrat", sans-serif; font-weight: 600; font-size: 57px; line-height: 64px; border-bottom: 2px solid var(--sky); }
  .person__role { font-size: 25px; line-height: 30px; }

  .contact { position: absolute; left: 688px; top: 993px; color: var(--sky); font-size: 20.5px; line-height: 26.5px; }
  .contact__row { display: flex; }
  .contact__label { width: 68px; }
</style>
</head>
<body>
<div class="canvas">
  <div class="crop-mark crop-mark--left"></div>
  <div class="crop-mark crop-mark--right"></div>

  <div class="brand">
    <span class="brand__mark"></span>
    <span class="brand__name">Kelbrook Systems Ltd.</span>
  </div>

  <div class="tagline">Revolutionizing IT Services</div>

  <div class="band band--top" role="img" aria-label="Decorative blue wave band"></div>

  <div class="person">
    <div class="person__name">Daniel Marsh</div>
    <div class="person__role">Network Engineer</div>
  </div>

  <div class="contact">
    <div class="contact__row"><span class="contact__label">E-mail</span><span>: dmarsh@kelbrook.me</span></div>
    <div class="contact__row"><span class="contact__label">Web</span><span>: kelbrook.me</span></div>
    <div class="contact__row"><span class="contact__label">Ph</span><span>: Ph: 604-555-0142</span></div>
  </div>

  <div class="band band--bottom" role="img" aria-label="Decorative blue wave band"></div>
</div>
</body>
</html>
```